Wordpress Design for my Consulting Company

We want a WordPress site created for our new business. We have created a mock-up of the content we want on the site at https://marcusdellow.example-sites.com/website-5

We are not attached to any of the pictures and just put stock stuff from wix's editor, which we don't have rights to use outside of wix.

We are NOT looking to just port this site to WordPress, we are looking for some creative ways to display the content in a more professional artistic sense.

I have included several logo files and a text file with the colors and Fonts used in the logo. We are not looking to change the logo or the colors used in the logo.

The Schedule appointment links to a page that embeds a bookingnest.example.com calendar. https://bookingnest.example.com/marcus-dellow/brightvale

The final website domain will be enterprisebrightvale.example

Enterprise brightvale is a consulting company that works directly with the business owners and leaders of small businesses between 50-200 employees. We help companies make sure they have the right technology to meet their strategic goals. We are the anti-"Computer Guy" and we focus on business outcomes NOT cool technology gadgets.

The final design should communicate business growth and success.

Target Market(s)

Business Owners of companies with 50-200 employees

Coding

Coded - Design and coding required

Number of Pages Required

1 page

Font styles to use
Serif
Other font styles liked:
• Trajan Pro Bold, Open Sans

Requirements
Must have
• Should focus on consulting rather than technology.
• Should show the customer as the hero and we are just their guide.
• Must use the logo provided and the colors and fonts in the text file provided. Any other colors and fonts must be complementary.
• The design should scale for all devices computer, iPad, or phone
Should not have
• Should not focus on technology, we are the anti-"Computer Guy" and we focus on business outcomes NOT cool technology gadgets.

```html
<!DOCTYPE html>
<html lang="en">
<head>
<meta charset="utf-8">
<title>Brightvale — Discover Your Business Path</title>
<link rel="stylesheet" href="https://fonts.googleapis.com/css2?family=Cinzel:wght@400;700&family=Open+Sans:ital,wght@0,400;0,600;0,700;1,400&display=swap">
<style>
:root{
  --orange:#bf6438;
  --orange-dark:#a9532b;
  --ink:#2d3438;
  --text:#555b60;
  --muted:#777d82;
  --mist:#eef1f4;
  --white:#ffffff;
  --footer:#3a4247;
  --line:rgba(255,255,255,.18);
}
*{box-sizing:border-box;margin:0;padding:0}
html,body{width:1200px;height:3429px;overflow:hidden}
body{position:relative;font-family:"Open Sans",Arial,sans-serif;color:var(--text);background:var(--white)}
.abs{position:absolute}
.serif{font-family:"Cinzel","Times New Roman",serif}

/* header */
.site-header{left:0;top:0;width:1200px;height:114px;background:var(--white)}
.brand{left:110px;top:10px;display:flex;align-items:center;gap:22px}
.brand-dot{width:92px;height:92px;border-radius:50%;background:var(--ink)}
.brand-name{font-family:"Cinzel",serif;font-weight:700;font-size:27px;color:var(--ink);line-height:1}
.brand-tag{font-family:"Cinzel",serif;font-size:12.5px;color:var(--ink);margin-top:5px;letter-spacing:.3px}
.top-contact{right:110px;top:22px;font-size:16px;color:var(--ink);display:flex;align-items:center;gap:12px}
.top-contact svg{fill:var(--orange);vertical-align:-3px;margin-right:6px}
.top-contact .sep{color:var(--muted)}
.main-nav{right:110px;top:70px;display:flex;gap:34px;font-size:15.5px;font-weight:600;color:var(--ink);align-items:center}
.main-nav .active{color:var(--orange)}

/* hero */
.hero{left:0;top:114px;width:1200px;height:556px;background:linear-gradient(180deg,#5b6e8c 0%,#a07a78 30%,#7a5a4c 55%,#3a3430 100%)}
.hero-title{left:0;width:1200px;text-align:center;color:var(--white);font-family:"Cinzel",serif;font-weight:700}
.hero-title.l1{top:212px;font-size:60px;letter-spacing:2px}
.hero-title.l2{top:288px;font-size:92px;letter-spacing:3px}
.btn-outline{border:2px solid var(--white);border-radius:40px;color:var(--white);font-weight:700;font-size:16px;text-align:center;letter-spacing:.5px}
.hero .btn-outline{position:absolute;left:457px;top:309px;width:286px;height:57px;line-height:53px}
.slide-arrow{top:254px;width:40px;height:52px;background:rgba(40,44,48,.55)}
.slide-arrow svg{display:block;margin:14px auto}

/* welcome */
.welcome-title{top:748px;left:0;width:1200px;text-align:center;font-size:52px;font-weight:700;color:var(--ink);letter-spacing:1px}
.welcome-text{top:832px;left:170px;width:860px;text-align:center;font-size:15.5px;line-height:31px;color:var(--muted)}
.step{top:949px;width:256px;height:276px;text-align:center;padding-top:26px}
.step svg{fill:var(--orange)}
.step h3{font-weight:400;font-size:29px;color:var(--ink);margin-top:18px}
.step p{font-size:14.5px;line-height:25px;color:var(--muted);margin:18px 16px 0}
.step.featured{background:var(--ink)}
.step.featured svg{fill:var(--white)}
.step.featured h3,.step.featured p{color:var(--white)}

/* tired band */
.tired{left:0;top:1344px;width:1200px;height:484px;background:var(--mist)}
.tired-title{left:110px;top:132px;font-size:49px;font-weight:700;line-height:67px;color:var(--ink);letter-spacing:1px}
.pain-list{left:575px;top:76px;width:520px;list-style:none}
.pain-list li{position:relative;padding-left:38px;font-size:14.5px;line-height:22px;color:var(--text);margin-bottom:20px}
.pain-list svg{position:absolute;left:0;top:2px}

/* split */
.split-photo{left:0;top:1828px;width:600px;height:474px;background:linear-gradient(135deg,#8a9aab 0%,#5d6775 45%,#2b313a 100%)}
.split-copy{left:600px;top:1828px;width:600px;height:474px;background:var(--orange);color:var(--white);padding:82px 80px 0 51px}
.split-copy p{font-size:14.5px;line-height:26px;margin-bottom:26px}
.split-copy .btn-outline{display:block;width:286px;height:58px;line-height:54px;margin-top:22px}

/* testimonials */
.testi-title{top:2422px;left:0;width:1200px;text-align:center;font-size:48px;font-weight:700;color:var(--ink);letter-spacing:1px}
.avatar{left:550px;top:2510px;width:100px;height:100px;border-radius:50%;background:linear-gradient(180deg,#d9b56a,#6b5a48);border:3px solid var(--white);box-shadow:0 0 0 2px #e6d9b8}
.circle-arrow{top:2642px;width:48px;height:48px;border:2px solid #9aa0a5;border-radius:50%}
.circle-arrow svg{display:block;margin:13px auto}
.quote{top:2642px;left:190px;width:820px;text-align:center;font-style:italic;font-size:16px;line-height:34px;color:var(--text)}
.quote-by{top:2726px;left:0;width:1200px;text-align:center;font-size:19px;color:var(--ink)}
.quote-by strong{font-weight:600}

/* footer */
.site-footer{left:0;top:2869px;width:1200px;height:560px;background:linear-gradient(135deg,#4a5257 0%,#343b40 55%,#2a3034 100%)}
.footer-heading{font-family:"Cinzel",serif;font-weight:700;font-size:23px;color:var(--white);letter-spacing:1px}
.field{position:absolute;background:var(--white);border:1px solid #c9cdd0;font-size:12px;color:#6c7277;padding:7px 12px}
.btn-submit{left:633px;top:370px;width:112px;height:46px;border-radius:24px;background:var(--orange);color:var(--white);font-size:14px;font-weight:700;text-align:center;line-height:46px;letter-spacing:.5px}
.info-row{left:805px;display:flex;gap:22px;align-items:flex-start;color:var(--white);font-size:14.5px;line-height:25px}
.info-icon{width:34px;height:34px;border-radius:50%;border:1.5px solid rgba(255,255,255,.45);flex:none;display:flex;align-items:center;justify-content:center}
.info-icon svg{fill:var(--orange)}
.social{left:805px;top:362px;display:flex;gap:12px}
.social span{width:30px;height:30px;border-radius:50%;display:block}
.footer-rule{left:110px;top:457px;width:980px;height:1px;background:var(--line)}
.copyright{left:0;top:488px;width:1200px;text-align:center;color:var(--white);font-size:14px}
</style>
</head>
<body>

<header class="site-header abs">
  <div class="brand abs">
    <span class="brand-dot"></span>
    <div>
      <div class="brand-name">Brightvale</div>
      <div class="brand-tag">Discover Your Business Path</div>
    </div>
  </div>
  <div class="top-contact abs">
    <span><svg width="16" height="16" viewBox="0 0 24 24"><path d="M6.6 10.8a15.5 15.5 0 0 0 6.6 6.6l2.2-2.2c.3-.3.7-.4 1-.2 1.1.4 2.3.6 3.6.6.6 0 1 .4 1 1V20c0 .6-.4 1-1 1A17 17 0 0 1 3 4c0-.6.4-1 1-1h3.5c.6 0 1 .4 1 1 0 1.3.2 2.5.6 3.6.1.3 0 .7-.2 1z"/></svg>(555) 014-2270</span>
    <span class="sep">|</span>
    <span><svg width="17" height="15" viewBox="0 0 24 20"><path d="M2 2h20c1 0 2 1 2 2v.5l-12 7-12-7V4c0-1 1-2 2-2zm-2 5 12 7 12-7v10c0 1-1 2-2 2H2c-1 0-2-1-2-2z"/></svg>mdellow@enterprisebrightvale.example</span>
  </div>
  <nav class="main-nav abs">
    <span class="active">HOME</span><span>ABOUT US</span><span>SERVICES</span><span>BLOG</span><span>CONTACT</span>
    <svg width="16" height="16" viewBox="0 0 24 24" fill="none" stroke="#2d3438" stroke-width="3"><circle cx="10" cy="10" r="7"/><path d="M15 15l7 7"/></svg>
  </nav>
</header>

<section class="hero abs" role="img" aria-label="Photograph of a downtown city skyline at sunset">
  <div class="slide-arrow abs" style="left:0"><svg width="14" height="24" viewBox="0 0 14 24" fill="none" stroke="#fff" stroke-width="3"><path d="M12 2 2 12l10 10"/></svg></div>
  <div class="slide-arrow abs" style="right:0"><svg width="14" height="24" viewBox="0 0 14 24" fill="none" stroke="#fff" stroke-width="3"><path d="M2 2l10 10L2 22"/></svg></div>
  <span class="btn-outline">SCHEDULE APPOINTMENT</span>
</section>
<h1 class="hero-title l1 abs">DISCOVER YOUR</h1>
<div class="hero-title l2 abs">BUSINESS PATH</div>

<h2 class="welcome-title abs serif">WELCOME TO BRIGHTVALE</h2>
<p class="welcome-text abs">We get the frustration of working with consultants and experts who don't listen or take the time to understand your company goals and vision. We believe technology should serve your business, not the other way around.</p>

<div class="step abs" style="left:91px">
  <svg width="64" height="64" viewBox="0 0 64 64"><path d="M26 4a22 22 0 0 1 17.6 35.2L60 55.6 55.6 60 39.2 43.6A22 22 0 1 1 26 4zm0 8a14 14 0 1 0 0 28 14 14 0 0 0 0-28z"/></svg>
  <h3>Discover</h3>
  <p>Identify what is going on behind the scenes, and create a snapshot of the current infrastructure.</p>
</div>
<div class="step featured abs" style="left:345px">
  <svg width="72" height="60" viewBox="0 0 72 60"><path d="M0 0h5v55h67v5H0z"/><rect x="14" y="30" width="8" height="20"/><rect x="27" y="18" width="8" height="32"/><rect x="40" y="24" width="8" height="26"/><rect x="53" y="8" width="8" height="42"/></svg>
  <h3>Prioritize</h3>
  <p>Meet to decide which solutions and policies will have the greatest impact on reaching the companies goals.</p>
</div>
<div class="step abs" style="left:599px">
  <svg width="72" height="64" viewBox="0 0 72 64"><path d="M24 12l4 0 1 6 5 2 5-4 3 3-4 5 2 5 6 1v4l-6 1-2 5 4 5-3 3-5-4-5 2-1 6h-4l-1-6-5-2-5 4-3-3 4-5-2-5-6-1v-4l6-1 2-5-4-5 3-3 5 4 5-2zm2 14a6 6 0 1 0 0 12 6 6 0 0 0 0-12zM54 0h3l1 4 3 1 3-2 2 2-2 3 1 3 4 1v3l-4 1-1 3 2 3-2 2-3-2-3 1-1 4h-3l-1-4-3-1-3 2-2-2 2-3-1-3-4-1v-3l4-1 1-3-2-3 2-2 3 2 3-1zm1.5 9a3.5 3.5 0 1 0 0 7 3.5 3.5 0 0 0 0-7zM54 38h3l1 4 3 1 3-2 2 2-2 3 1 3 4 1v3l-4 1-1 3 2 3-2 2-3-2-3 1-1 4h-3l-1-4-3-1-3 2-2-2 2-3-1-3-4-1v-3l4-1 1-3-2-3 2-2 3 2 3-1zm1.5 9a3.5 3.5 0 1 0 0 7 3.5 3.5 0 0 0 0-7z"/></svg>
  <h3>Implement</h3>
  <p>Implement those things that will give the greatest return on investment.</p>
</div>
<div class="step abs" style="left:853px">
  <svg width="64" height="64" viewBox="0 0 64 64"><path d="M46 2a16 16 0 0 0-15 21L4 50a7 7 0 0 0 10 10l27-27A16 16 0 0 0 62 18l-9 9-9-3-3-9 9-9a16 16 0 0 0-4-4zM9 52a3 3 0 1 1 0 6 3 3 0 0 1 0-6z"/></svg>
  <h3>Maintain</h3>
  <p>Create a system that keeps your technology aligned as strategy adjusts over time.</p>
</div>

<section class="tired abs">
  <h2 class="tired-title abs serif">ARE YOU TIRED<br>OF "COMPUTER<br>GUYS" THAT...</h2>
  <ul class="pain-list abs">
    <li><svg width="17" height="17" viewBox="0 0 20 20"><circle cx="10" cy="10" r="10" fill="#bf6438"/><path d="M5.5 10.5l3 3 6-6.5" fill="none" stroke="#fff" stroke-width="2.4"/></svg>Don't want to be involved in business strategy.</li>
    <li><svg width="17" height="17" viewBox="0 0 20 20"><circle cx="10" cy="10" r="10" fill="#bf6438"/><path d="M5.5 10.5l3 3 6-6.5" fill="none" stroke="#fff" stroke-width="2.4"/></svg>Say "No!" but do not give options on how to achieve your business outcome.</li>
    <li><svg width="17" height="17" viewBox="0 0 20 20"><circle cx="10" cy="10" r="10" fill="#bf6438"/><path d="M5.5 10.5l3 3 6-6.5" fill="none" stroke="#fff" stroke-width="2.4"/></svg>Can't explain how a technology will create business value, but insist it is necessary.</li>
    <li><svg width="17" height="17" viewBox="0 0 20 20"><circle cx="10" cy="10" r="10" fill="#bf6438"/><path d="M5.5 10.5l3 3 6-6.5" fill="none" stroke="#fff" stroke-width="2.4"/></svg>Give you the excuse, "You never asked."</li>
    <li><svg width="17" height="17" viewBox="0 0 20 20"><circle cx="10" cy="10" r="10" fill="#bf6438"/><path d="M5.5 10.5l3 3 6-6.5" fill="none" stroke="#fff" stroke-width="2.4"/></svg>Recommend technology when a simple process or policy change would have the same effect.</li>
    <li><svg width="17" height="17" viewBox="0 0 20 20"><circle cx="10" cy="10" r="10" fill="#bf6438"/><path d="M5.5 10.5l3 3 6-6.5" fill="none" stroke="#fff" stroke-width="2.4"/></svg>Suggest expensive solutions that are just thrown away, soon after they are deployed.</li>
  </ul>
</section>

<div class="split-photo abs" role="img" aria-label="Photograph of three business professionals reviewing documents together"></div>
<section class="split-copy abs">
  <p>Computer guys frustrate business leaders because they don't have a business mindset. Brightvale advises on strategy that helps companies apply technology to gain a competitive advantage.</p>
  <p>Businesses spend a lot of time and money on books, coaches and consultants creating a great strategy but still struggle to achieve their goals. Brightvale has a discovery process that reveals what is getting in the way of executing their strategy.</p>
  <span class="btn-outline">SCHEDULE APPOINTMENT</span>
</section>

<h2 class="testi-title abs serif">TESTIMONIALS</h2>
<div class="avatar abs" role="img" aria-label="Portrait photo of the client giving the testimonial"></div>
<div class="circle-arrow abs" style="left:32px"><svg width="12" height="18" viewBox="0 0 12 18" fill="none" stroke="#555b60" stroke-width="2.5"><path d="M10 1 2 9l8 8"/></svg></div>
<div class="circle-arrow abs" style="left:1120px"><svg width="12" height="18" viewBox="0 0 12 18" fill="none" stroke="#555b60" stroke-width="2.5"><path d="M2 1l8 8-8 8"/></svg></div>
<p class="quote abs">"I knew I was behind, I just didn't know by how much. &nbsp;We had years of band-aided solutions and Brightvale helped us stabilize our environment and position ourselves to compete in the quickly changing world of copy and print"</p>
<p class="quote-by abs"><strong>-Dana Whitlock,</strong> Print Harbor</p>

<footer class="site-footer abs" role="img" aria-label="Dimmed photograph of business people at a meeting table">
  <h3 class="footer-heading abs" style="left:110px;top:105px">CONTACT FORM</h3>
  <div class="field" style="left:113px;top:176px;width:310px;height:33px">First Name</div>
  <div class="field" style="left:432px;top:176px;width:310px;height:33px">Last Name</div>
  <div class="field" style="left:113px;top:224px;width:310px;height:33px">Email</div>
  <div class="field" style="left:432px;top:224px;width:310px;height:33px">Phone Number</div>
  <div class="field" style="left:113px;top:269px;width:629px;height:83px">Comments</div>
  <div class="btn-submit abs">SUBMIT</div>

  <h3 class="footer-heading abs" style="left:805px;top:105px">CONTACT INFORMATION</h3>
  <div class="info-row abs" style="top:172px">
    <span class="info-icon"><svg width="12" height="16" viewBox="0 0 12 16"><path d="M6 0a6 6 0 0 1 6 6c0 4-6 10-6 10S0 10 0 6a6 6 0 0 1 6-6zm0 3.5a2.5 2.5 0 1 0 0 5 2.5 2.5 0 0 0 0-5z"/></svg></span>
    <span>4120 Harlow Parkway South, Suite 200<br>Westbrook, TX 77001</span>
  </div>
  <div class="info-row abs" style="top:236px">
    <span class="info-icon"><svg width="14" height="14" viewBox="0 0 24 24"><path d="M6.6 10.8a15.5 15.5 0 0 0 6.6 6.6l2.2-2.2c.3-.3.7-.4 1-.2 1.1.4 2.3.6 3.6.6.6 0 1 .4 1 1V20c0 .6-.4 1-1 1A17 17 0 0 1 3 4c0-.6.4-1 1-1h3.5c.6 0 1 .4 1 1 0 1.3.2 2.5.6 3.6.1.3 0 .7-.2 1z"/></svg></span>
    <span style="line-height:34px">(555) 014-2270</span>
  </div>
  <div class="info-row abs" style="top:294px">
    <span class="info-icon"><svg width="15" height="12" viewBox="0 0 24 20"><path d="M2 2h20c1 0 2 1 2 2v.5l-12 7-12-7V4c0-1 1-2 2-2zm-2 5 12 7 12-7v10c0 1-1 2-2 2H2c-1 0-2-1-2-2z"/></svg></span>
    <span style="line-height:34px">mdellow@enterprisebrightvale.example</span>
  </div>
  <div class="social abs">
    <span style="background:#3b5998"></span>
    <span style="background:#b0694a"></span>
    <span style="background:#d9483b"></span>
    <span style="background:#c4302b"></span>
  </div>
  <div class="footer-rule abs"></div>
  <p class="copyright abs">Copyright © 2018, &nbsp;Brightvale. All rights reserved.</p>
</footer>

</body>
</html>
```